Saltmarsh Motocross Club. Sports club.

We are a family orientated Motocross Club in Saltmarsh Bay. We have 3 motocross tracks, Intermediate Track, Junior rack and E-track. We also have a School(Academy) and maintenance facility that caters for all motorbike services. We have a BBQ area with a 20x70 meter pool after a hot day of riding. We are busy adding a restaurant and bar in the next few weeks. We host 6 Club races in the season as well as the Crescent Ridge Championship. Therefore we will need a race calendar as well as race results page. The school have a dedicated school facility with bike rental, bike show room, gear rental and small shop. We have instructors that instruct kids from 4 years old to professional riders.

Target Market(s)

Motocross riders, kids from 4 years

Industry/Entity Type

extreme sports, motorsports motocross

Coding

Coded - Design and coding required

Number of Pages Required

5+ page

Font styles to use
Sans Serif

Colors

Designer to choose colors to be used in the design.

Requirements
Must have
• User Friendly, Easy to update, Calendar , online payment, race results, academy, facilities,
Nice to have
• Just an update it has to have a calendar with sides that shows whats happening on the day. We also need at the top of page the "open hours", " a next event" button, our partners button at the bottom of page a "News Page" "testimonials" with all the necessary links, social medial, address, contact details, etc.
Should not have
• no cartoons or any clipart please just photos

```html
<!DOCTYPE html>
<html lang="en">
<head>
<meta charset="utf-8">
<title>Saltmarsh Motocross Club</title>
<link href="https://fonts.googleapis.com/css2?family=Oswald:wght@500;600;700&family=Work+Sans:wght@400;500;600&display=swap" rel="stylesheet">
<style>
:root{
  --red:#e4232b;
  --black:#0b0b0b;
  --ink:#1c1c1c;
  --muted:#8a8a8a;
  --line:#e3e3e3;
  --white:#ffffff;
  --head:'Oswald',sans-serif;
  --body:'Work Sans',sans-serif;
}
*{margin:0;padding:0;box-sizing:border-box}
html,body{width:1200px;height:4847px;overflow:hidden;background:var(--white);font-family:var(--body);color:var(--ink)}
.page{position:relative;width:1200px;height:4847px}
.abs{position:absolute}
.outline{color:transparent;-webkit-text-stroke:1.3px #9a9a9a}
.label{font-family:var(--head);font-weight:500;font-size:13px;letter-spacing:.5px;color:var(--red);text-transform:uppercase;display:flex;align-items:center;gap:12px}
.label::before{content:"";width:28px;height:2px;background:var(--red)}
.h2{font-family:var(--head);font-weight:600;font-size:40px;line-height:1.1;text-transform:uppercase;letter-spacing:.5px}
.btn{position:absolute;background:var(--red);color:var(--white);font-family:var(--head);font-weight:500;font-size:12px;letter-spacing:.5px;text-transform:uppercase;display:flex;align-items:center;justify-content:center;gap:12px}
.arrow{width:26px;height:8px}
p{font-size:13px;line-height:21px;color:var(--muted)}

.topbar{top:0;left:0;width:1200px;height:45px;border-bottom:1px solid var(--line);font-size:12.5px;color:#555}
.topbar .item{position:absolute;top:14px;display:flex;align-items:center;gap:8px}
.topbar svg{width:12px;height:12px}
.social{position:absolute;display:flex;gap:14px}
.social span{width:10px;height:10px;border-radius:50%;border:1.5px solid currentColor}
.header{top:45px;left:0;width:1200px;height:90px}
.brand{position:absolute;display:flex;align-items:center;gap:8px;font-family:var(--head);font-weight:700;font-size:22px;letter-spacing:.5px;text-transform:uppercase}
.brand i{width:14px;height:14px;background:var(--red)}
.nav{position:absolute;top:36px;left:376px;display:flex;gap:26px;font-family:var(--head);font-weight:500;font-size:12px;text-transform:uppercase}
.nav .on{color:var(--red)}
.hero{top:135px;left:0;width:1200px;height:540px;background:linear-gradient(110deg,#c8302a 0%,#d9a52a 22%,#3b3f52 45%,#6d6a63 70%,#a08f70 100%)}
.hero-title{position:absolute;right:87px;top:105px;text-align:right;font-family:var(--head);font-weight:600;font-size:84px;line-height:92px;color:var(--white);text-transform:uppercase}
.hero-title .outline{-webkit-text-stroke:1.5px var(--white)}
.hero p{position:absolute;right:87px;top:307px;width:470px;text-align:right;color:#eee;font-size:13px}
.slider{position:absolute;left:86px;top:486px;width:121px;height:54px;background:var(--white);display:flex}
.slider div{flex:1;display:flex;align-items:center;justify-content:center}
.card{position:absolute;top:867px;width:237px;height:177px;border:1px solid var(--line);border-bottom:4px solid var(--red);padding:27px 26px}
.card small{font-family:var(--head);font-size:10px;text-transform:uppercase;display:block}
.card b{font-family:var(--head);font-weight:500;font-size:17px;text-transform:uppercase;display:block;margin-top:2px}
.card .plus{position:absolute;left:24px;bottom:24px;font-size:26px;font-weight:300}
.card .ico{position:absolute;right:26px;bottom:22px;width:48px;height:48px;border:2px solid #e6e6e6;border-radius:50%}
.card.active{background:var(--red);color:var(--white)}
.card.active .ico{border-color:var(--white)}
.offer{top:1796px;left:0;width:1200px;height:728px;background:var(--black);color:var(--white)}
.ocard{position:absolute;top:200px;width:237px}
.ocard .ph{height:342px}
.ocard .num{position:absolute;right:10px;top:310px;font-family:var(--head);font-size:62px;line-height:1;color:transparent;-webkit-text-stroke:1.3px #888}
.ocard small{display:flex;align-items:center;gap:10px;margin-top:48px;font-family:var(--head);font-size:11px;text-transform:uppercase}
.ocard small::after{content:"";width:30px;height:1px;background:#888}
.ocard b{display:block;margin-top:4px;font-family:var(--head);font-weight:500;font-size:18px;text-transform:uppercase}
.field{position:absolute;left:536px;width:527px;border:1px solid #d8d8d8;font-size:12px;color:#999;padding:24px 22px 0}
.footer{top:4618px;left:0;width:1200px;height:229px;background:var(--black);color:var(--white)}
.fnav{position:absolute;top:74px;left:276px;display:flex;gap:39px;font-family:var(--head);font-size:12px;text-transform:uppercase}
</style>
</head>
<body>
<div class="page">

<div class="abs topbar">
  <div class="item" style="left:86px"><svg viewBox="0 0 12 12"><path d="M2 1l2.5 0 1 3-1.5 1a7 7 0 003 3l1-1.5 3 1V10A1.5 1.5 0 019.5 11.5 9.5 9.5 0 01.5 2.5 1.5 1.5 0 012 1z" fill="#e4232b"/></svg>01 - 555 - 0199</div>
  <div class="item" style="left:225px"><svg viewBox="0 0 12 12"><rect x="0" y="2" width="12" height="8" fill="#e4232b"/><path d="M0 2l6 4 6-4" stroke="#fff" fill="none"/></svg>info@saltmarsh-mx.example</div>
  <div class="item" style="left:428px"><svg viewBox="0 0 12 12"><path d="M6 0a4 4 0 014 4c0 3-4 8-4 8S2 7 2 4a4 4 0 014-4z" fill="#e4232b"/><circle cx="6" cy="4" r="1.5" fill="#fff"/></svg>Harbour Loop Rd - Saltmarsh - UAE</div>
  <div class="social" style="left:1045px;top:17px;color:#444"><span></span><span></span><span></span></div>
</div>

<header class="abs header">
  <div class="brand" style="left:86px;top:30px"><i></i>Saltmarsh MX</div>
  <nav class="nav"><span class="on">Home</span><span>About</span><span>Races</span><span>Calendar</span><span>Academy</span><span>BBQ</span><span>Gallery</span><span>Contact</span></nav>
  <svg class="abs" style="left:902px;top:38px" width="14" height="14" viewBox="0 0 14 14"><circle cx="6" cy="6" r="4.5" stroke="#222" stroke-width="1.6" fill="none"/><path d="M9.5 9.5l3 3" stroke="#222" stroke-width="1.6"/></svg>
  <div class="btn" style="left:938px;top:25px;width:175px;height:41px">Upcoming Events <svg class="arrow" viewBox="0 0 26 8"><path d="M0 4h24M20 1l4 3-4 3" stroke="#fff" fill="none"/></svg></div>
</header>

<section class="abs hero" role="img" aria-label="Close-up of a motocross rider in a colourful helmet and goggles">
  <h1 class="hero-title">Riding Makes<br>One <span class="outline">Happy</span></h1>
  <p>We are a family orientated Motocross Club in Saltmarsh Bay. We have 3 motocross tracks, Intermediate Track, Junior rack and E-track.</p>
  <div class="btn" style="right:87px;top:369px;width:175px;height:41px"><svg class="arrow" viewBox="0 0 26 8"><path d="M26 4H2M6 1L2 4l4 3" stroke="#fff" fill="none"/></svg> Join Our Club</div>
  <div class="abs" style="left:1100px;top:442px;width:66px;height:66px;border-radius:50%;border:2px solid rgba(255,255,255,.5)"></div>
  <div class="slider">
    <div><svg width="10" height="16" viewBox="0 0 10 16"><path d="M8 1L2 8l6 7" stroke="#111" stroke-width="2" fill="none"/></svg></div>
    <div><svg width="10" height="16" viewBox="0 0 10 16"><path d="M2 1l6 7-6 7" stroke="#bbb" stroke-width="2" fill="none"/></svg></div>
  </div>
</section>

<section>
  <div class="abs label" style="left:86px;top:772px">What We Provide</div>
  <h2 class="abs h2" style="left:86px;top:797px">Accelerating Your <span class="outline">Riding</span></h2>
  <div class="card active" style="left:86px"><small>Information in detail</small><b>Race Information</b><span class="plus">+</span><span class="ico"></span></div>
  <div class="card" style="left:350px"><small>Expert volunteers</small><b>Club Volunteers</b><span class="plus">+</span><span class="ico"></span></div>
  <div class="card" style="left:613px"><small>From SMX</small><b>Riding Contest</b><span class="plus">+</span><span class="ico"></span></div>
  <div class="card" style="left:877px"><small>For the practice</small><b>Our Academy</b><span class="plus">+</span><span class="ico"></span></div>
</section>

<section>
  <div class="abs" style="left:0;top:1145px;width:235px;height:550px;background:var(--red)"></div>
  <div class="abs" style="left:86px;top:1191px;width:461px;height:459px;background:linear-gradient(180deg,#2a2a2a 0%,#6b6b6b 35%,#e8e8e8 60%,#f3f3f3 100%)" role="img" aria-label="Motocross rider on a bike in front of a club banner"></div>
  <div class="abs label" style="left:613px;top:1222px">About Us</div>
  <h2 class="abs h2" style="left:613px;top:1247px;font-size:38px">Welcome Home of SMX<br><span class="outline">Motocross</span></h2>
  <p class="abs" style="left:613px;top:1354px;width:470px">We are a family orientated Motocross Club in Saltmarsh Bay. We have 3 motocross tracks, Intermediate Track, Junior rack and E-track. We also have a School (Academy) and maintenance facility that caters for all motorbike services.</p>
  <div class="abs" style="left:613px;top:1465px;width:220px">
    <div style="font-family:var(--head);font-weight:500;font-size:13px;text-transform:uppercase;display:flex;gap:10px;align-items:center"><svg class="arrow" style="width:20px" viewBox="0 0 26 8"><path d="M0 4h24M20 1l4 3-4 3" stroke="#e4232b" stroke-width="1.5" fill="none"/></svg>Ready for the racing</div>
    <p style="margin-top:8px">Lorem Ipsum is simply dummy text of the printing</p>
  </div>
  <div class="abs" style="left:859px;top:1465px;width:220px">
    <div style="font-family:var(--head);font-weight:500;font-size:13px;text-transform:uppercase;display:flex;gap:10px;align-items:center"><svg class="arrow" style="width:20px" viewBox="0 0 26 8"><path d="M0 4h24M20 1l4 3-4 3" stroke="#e4232b" stroke-width="1.5" fill="none"/></svg>Ready for the racing</div>
    <p style="margin-top:8px">Lorem Ipsum is simply dummy text of the printing</p>
  </div>
  <div class="btn" style="left:613px;top:1556px;width:175px;height:39px">More About Us <svg class="arrow" viewBox="0 0 26 8"><path d="M0 4h24M20 1l4 3-4 3" stroke="#fff" fill="none"/></svg></div>
</section>

<section class="abs offer">
  <div class="abs label" style="left:86px;top:96px">Our Races</div>
  <h2 class="abs h2" style="left:86px;top:121px;color:var(--white)">What We Offer In <span class="outline">Our Club</span></h2>
  <div class="abs" style="left:1035px;top:121px;width:39px;height:39px;background:var(--white);display:flex;align-items:center;justify-content:center"><svg width="8" height="14" viewBox="0 0 8 14"><path d="M7 1L1 7l6 6" stroke="#e4232b" stroke-width="2" fill="none"/></svg></div>
  <div class="abs" style="left:1074px;top:121px;width:39px;height:39px;background:var(--red);display:flex;align-items:center;justify-content:center"><svg width="8" height="14" viewBox="0 0 8 14"><path d="M1 1l6 6-6 6" stroke="#fff" stroke-width="2" fill="none"/></svg></div>
  <div class="ocard" style="left:86px"><div class="ph" role="img" aria-label="Young rider in protective gear at the track" style="background:linear-gradient(180deg,#cfc9c0,#6d5e4e)"></div><span class="num">01</span><small>Coaching</small><b>Private Coaching</b></div>
  <div class="ocard" style="left:350px"><div class="ph" role="img" aria-label="Rider on a classic motocross bike" style="background:linear-gradient(180deg,#b2302a,#2a3a7c 60%,#8a8a8a)"></div><span class="num">02</span><small>Motorcycle</small><b>Classic Motorcycle</b></div>
  <div class="ocard" style="left:613px"><div class="ph" role="img" aria-label="Rider kicking up sand on a dune" style="background:linear-gradient(180deg,#5a4a2c,#c9a35a)"></div><span class="num">03</span><small>Performance</small><b>Strenuous Bikers</b></div>
  <div class="ocard" style="left:877px"><div class="ph" role="img" aria-label="Group of riders at the race start" style="background:linear-gradient(180deg,#9fa2a8,#5b4d42)"></div><span class="num">04</span><small>Riders team</small><b>Adventure Riding</b></div>
</section>

<section>
  <div class="abs label" style="left:0;width:1200px;top:2621px;justify-content:center"><span>Our Gallery</span><span style="width:28px;height:2px;background:var(--red)"></span></div>
  <h2 class="abs h2" style="left:0;width:1200px;top:2647px;text-align:center">A Place of <span class="outline">Discovery</span></h2>
  <div class="abs" style="left:86px;top:2731px;width:324px;height:316px;background:linear-gradient(160deg,#b79c6a,#8a6d3d)" role="img" aria-label="Rider sliding through a sandy corner"></div>
  <div class="abs" style="left:438px;top:2731px;width:324px;height:175px;background:linear-gradient(90deg,#e9ebee,#6b6560)" role="img" aria-label="Club members talking at the track"></div>
  <div class="abs" style="left:788px;top:2731px;width:325px;height:175px;background:linear-gradient(180deg,#5d7aa0,#2b2b2b)" role="img" aria-label="Finish line gantry against a blue sky"></div>
  <div class="abs" style="left:438px;top:2927px;width:324px;height:175px;background:linear-gradient(180deg,#d7dbe0,#9ea3a8)" role="img" aria-label="Bike showroom interior"></div>
  <div class="abs" style="left:788px;top:2927px;width:325px;height:175px;background:linear-gradient(180deg,#b7a98f,#705e45)" role="img" aria-label="Clubhouse in the desert at sunset"></div>
</section>

<section>
  <div class="abs label" style="left:86px;top:3280px">BBQ Area</div>
  <h2 class="abs h2" style="left:86px;top:3305px;font-size:38px">We Have a BBQ Area<br><span class="outline">With a Pool</span></h2>
  <p class="abs" style="left:86px;top:3412px;width:455px">We have a BBQ area with a 20x70 meter pool after a hot day of riding. We are busy adding a restaurant and bar in the next few weeks. We host 6 Club races in the season as well as the Crescent Ridge Championship. Therefore we will need a race calendar as well as race results page.</p>
  <p class="abs" style="left:86px;top:3527px;width:455px">The school have a dedicated school facility with bike rental, bike show room, gear rental and small shop. We have instructors that instruct kids from 4 years old to professional riders.</p>
  <div class="btn" style="left:86px;top:3613px;width:149px;height:40px">Learn More <svg class="arrow" viewBox="0 0 26 8"><path d="M0 4h24M20 1l4 3-4 3" stroke="#fff" fill="none"/></svg></div>
  <div class="abs" style="left:600px;top:3203px;width:600px;height:533px;background:linear-gradient(180deg,#9ec3c7 0%,#6aa3a8 40%,#4f7a3a 70%,#3e5a2e 100%)" role="img" aria-label="Children playing by the pool on a grass deck"></div>
</section>

<section>
  <div class="abs" style="left:86px;top:3835px;width:1027px;height:685px;background:var(--white);box-shadow:0 4px 24px rgba(0,0,0,.08)"></div>
  <div class="abs" style="left:86px;top:3835px;width:412px;height:685px;background:linear-gradient(160deg,#f3eee2,#efe9da 60%,#e8e2d2)" role="img" aria-label="Map showing the club location"></div>
  <div class="abs" style="left:438px;top:3905px;width:384px;height:59px;background:var(--white);box-shadow:0 4px 16px rgba(0,0,0,.12);border-left:12px solid var(--red);font-family:var(--head);font-weight:600;font-size:34px;line-height:59px;padding-left:70px;text-transform:uppercase">Get In Touch</div>
  <div class="field" style="top:4014px;height:64px">Your Name</div>
  <div class="field" style="top:4102px;height:64px">Your Email</div>
  <div class="field" style="top:4191px;height:64px">Subject</div>
  <div class="field" style="top:4281px;height:117px">Message</div>
  <div class="btn" style="left:931px;top:4420px;width:134px;height:42px">Submit Now</div>
</section>

<footer class="abs footer">
  <div class="brand" style="left:86px;top:52px;color:var(--white)"><i></i>Saltmarsh MX</div>
  <nav class="fnav"><span>Home</span><span>About</span><span>Races</span><span>Calendar</span><span>Academy</span><span>BBQ</span><span>Gallery</span><span>Contact</span></nav>
  <div class="social" style="left:1008px;top:76px;gap:26px;color:var(--white)"><span></span><span></span><span></span></div>
  <div class="abs" style="left:86px;top:145px;width:1027px;height:1px;background:#333"></div>
  <div class="abs" style="left:0;width:1200px;top:168px;text-align:center;font-size:12.5px">© SMX Motocross 2022 All rights reserved.</div>
</footer>

</div>
</body>
</html>
```